Modern and appealing business Wordpress site

I've been operating my consulting firm for 5 years and feel like it is time to really improve on my web presence as I'm starting to get more national attention. I had a logo made through this service a couple of years ago, and would like to get a website that matches the look of it. The website will be used to (1) advertise my services (2) provide a brief overview of our management philosophies, and (3) host a resource library database. I understand HTML, but am not as familiar with how to code Wordpress, so I need someone that can help upload themes.

The website can be found at www.trelmondgroup.com.

For design, I prefer round designs to square and want the color scheme to match the attached logo. I have included both the full logo and the abbreviated one.

I also have a new picture for CFO uploaded. I plan on getting a new one for the CEO in the coming weeks, so I would like someone that I could get to help make the modification at a later time.

The resource database will be put into a document library (probably Kiln7) once the final design is completed rather than having multiple pages with links...just so you know the final vision for the site.

Reach out if you have any questions.

Target Market(s)

Community Action Agencies, Nonprofit Organization Leaders

Industry/Entity Type

Consulting

Coding

Coded - Design and coding required

Font styles to use
Sans Serif

Requirements
Must have
• Must match the color scheme of the attached logo

```html
<!DOCTYPE html>
<html lang="en">
<head>
<meta charset="utf-8">
<title>Trelmond Group — Leading Organizations to Excellence</title>
<link rel="stylesheet" href="https://fonts.googleapis.com/css2?family=Poppins:wght@300;400;500;600;700&display=swap">
<style>
:root{
  --blue:#2fa6dc;
  --blue-deep:#0f78b8;
  --ink:#1b1b1b;
  --text:#555;
  --dark:#58585a;
  --darker:#3f3f41;
  --white:#fff;
}
*{box-sizing:border-box;margin:0;padding:0}
html,body{width:1200px;height:3254px;overflow:hidden}
body{position:relative;font-family:'Poppins',sans-serif;color:var(--text);background:var(--white)}
.abs{position:absolute}

/* hero */
.hero{left:0;top:0;width:1200px;height:705px;
  background:
    radial-gradient(circle at 1110px 130px,rgba(255,250,200,.95) 0,rgba(230,240,120,.6) 90px,rgba(0,0,0,0) 260px),
    radial-gradient(ellipse at 420px 420px,rgba(120,190,40,.7) 0,rgba(0,0,0,0) 260px),
    linear-gradient(180deg,#2d5a1e 0%,#4f8a2a 35%,#3b5a22 60%,#5a3a35 80%,#4a2e3a 100%);}
.hero-cut{left:0;top:520px}
.nav{left:164px;top:23px;width:872px;height:78px;background:var(--white);border-radius:30px 30px 0 0;}
.brand{display:flex;align-items:center;gap:10px;font-weight:700;font-size:28px;color:var(--blue);letter-spacing:1px}
.brand-dot{width:34px;height:34px;border-radius:50%;background:var(--blue)}
.nav .brand{position:absolute;left:22px;top:20px}
.menu{position:absolute;right:36px;top:30px;display:flex;gap:28px;font-size:12px;color:#444}
.menu .on{position:relative}
.menu .on::after{content:"";position:absolute;left:-4px;right:-4px;top:36px;height:4px;background:var(--blue)}
.hero-copy{left:618px;top:250px;width:418px;color:var(--white)}
.hero-copy h1{font-weight:300;font-size:31px;line-height:1.1}
.hero-copy h1 b{display:block;font-weight:700;font-size:46px}
.hero-copy p{margin-top:12px;font-size:13.2px;line-height:21.5px;font-weight:300;text-align:justify}
.chev{left:588px;top:622px}

/* services */
.h2{font-size:38px;font-weight:400;color:var(--ink)}
.h2 b{font-weight:700}
.services-title{left:163px;top:788px}
.card{top:879px;width:256px}
.card .media{width:256px;height:242px;border-radius:0 34px 0 34px}
.card h3{margin-top:24px;font-size:18.5px;font-weight:500;color:var(--ink)}
.card p{margin-top:12px;font-size:12.6px;line-height:21.3px;font-weight:300;text-align:justify}

/* mission */
.mission{left:0;top:1512px;width:1200px;height:466px;background:linear-gradient(90deg,#2aa0d8,#0f7dbf)}
.mission svg{position:absolute;left:0;top:0}
.mission-copy{left:633px;top:1668px;width:405px;color:var(--white)}
.mission-copy h2{font-size:37px;font-weight:400}
.mission-copy h2 b{font-weight:700}
.mission-copy p{margin-top:10px;font-size:18px;line-height:27.5px;font-weight:300}

/* testimonials */
.test-title{left:163px;top:2072px;font-weight:700}
.quote{top:2156px;width:415px;height:302px;border-top:14px solid var(--blue);border-bottom:14px solid var(--blue);border-radius:0 48px 0 48px;background:var(--white);padding:20px 22px}
.quote .mark{font-size:80px;line-height:60px;color:#e2e2e2;font-weight:700;font-family:Georgia,serif}
.quote .close{position:absolute;right:26px;bottom:8px}
.quote p{font-size:12.6px;line-height:21.4px;font-weight:300;color:#555}
.quote .who{margin-top:12px;padding-top:12px;font-size:12.6px;font-weight:500;color:#444;position:relative}
.quote .who::before{content:"";position:absolute;left:0;top:0;width:24px;height:3px;background:var(--blue)}
.arrow{top:2286px}

/* team */
.team{left:0;top:2606px;width:1200px;height:400px;background:var(--dark)}
.portrait{width:164px;height:164px;border-radius:50%;border:6px solid var(--white);top:2715px}
.role{color:var(--white);top:2775px;font-size:18px;font-weight:400;line-height:30px}
.role b{display:block;font-weight:400;font-size:16.5px}
.divider{left:587px;top:2715px;width:1px;height:165px;background:#8a8a8c}

/* footer */
.footer{left:0;top:2960px;width:1200px;height:262px}
.fcol{top:3055px;color:var(--white);font-size:11.5px;line-height:22px}
.fcol h4{font-size:15px;font-weight:500;margin-bottom:4px}
.fcol h4::after{content:"";display:block;width:22px;height:2px;background:var(--white);margin-top:4px}
.fsep{top:3018px;width:1px;height:160px;background:rgba(255,255,255,.45)}
.contact-row{display:flex;align-items:center;gap:9px}
.socials{display:flex;gap:14px;margin-top:6px}
.socials span{width:10px;height:10px;border-radius:50%;background:var(--white)}
.copy{left:0;top:3221px;width:1200px;height:33px;background:var(--darker);color:var(--white);font-size:11px;text-align:center;line-height:33px}
</style>
</head>
<body>

<section class="abs hero" role="img" aria-label="Hand pouring water onto a young green seedling growing from soil in sunlight"></section>
<svg class="abs hero-cut" width="1200" height="190" viewBox="0 0 1200 190" aria-hidden="true">
  <path d="M0 145 Q 480 225 1200 36 L1200 190 L0 190 Z" fill="#fff"/>
</svg>

<header class="abs nav">
  <div class="brand"><span class="brand-dot"></span>TRELMOND</div>
  <nav class="menu">
    <span class="on">Home</span><span>Services</span><span>Roma</span><span>Madd</span><span>Resources</span><span>Contact</span>
  </nav>
</header>

<div class="abs hero-copy">
  <h1>LEADING ORGANIZATIONS <b>TO EXCELLENCE!</b></h1>
  <p>Trelmond Group was created to help nonprofits and government contractors meet their basic funding requirements and adopt a Mission Aligned Data Driven mindset that promotes positive change in the lives of the people they serve. Our approach is not simply based off of theoretical business practices, but on practical solutions to real-life situations learned through more than twenty years of experience.</p>
</div>
<svg class="abs chev" width="24" height="14" viewBox="0 0 24 14" aria-hidden="true"><path d="M2 2 L12 11 L22 2" fill="none" stroke="#fff" stroke-width="2"/></svg>

<h2 class="abs h2 services-title">OUR <b>SERVICES</b></h2>

<article class="abs card" style="left:163px">
  <div class="media" role="img" aria-label="Consultants reviewing charts on paper beside a laptop" style="background:linear-gradient(135deg,#d9dde2,#9aa3ad)"></div>
  <h3>Training &amp; Consulting</h3>
  <p>We are dedicated to the success of our customers and offer a variety of services focused on improving organizational efficiency and effectiveness through implementation of the Mission Aligned Data Driven (MADD) mindset and the Results Oriented Management and Accountability (ROMA) system of organizational management.</p>
</article>
<article class="abs card" style="left:471px">
  <div class="media" role="img" aria-label="Glowing digital bar and line charts with numbers" style="background:linear-gradient(160deg,#0b2a3a,#13607a 55%,#0a3a4c)"></div>
  <h3>Data Analytics</h3>
  <p>One the most important, and frequently neglected, areas of organizational management is the analysis of data to accurately identify community needs and track progress towards the successful fulfillment of the entity's purpose. Our goal is to ensure each of our customers is equipped with the tools necessary to obtain objective data that will allow for quality decision making.</p>
</article>
<article class="abs card" style="left:779px">
  <div class="media" role="img" aria-label="Tablet with film strip and floating story panels" style="background:linear-gradient(160deg,#f1f2f4,#c9ccd0)"></div>
  <h3>Storytelling</h3>
  <p>Trelmond Group is dedicated to ensuring each of our customers is provided with the tools necessary to tell their story through the generation of graphic reports, outreach tools, and videos so they can increase community support and involvement, allowing for a reduced reliance on government funding.</p>
</article>

<section class="abs mission">
  <svg width="1200" height="466" viewBox="0 0 1200 466" role="img" aria-label="Compass dial pointing toward the word mission">
    <path d="M0 0 L215 0 Q 640 120 590 466 L0 466 Z" fill="#e8eef3"/>
  </svg>
</section>
<div class="abs mission-copy">
  <h2>OUR <b>MISSION</b></h2>
  <p>To help social service organizations develop a Mission Aligned Data Driven mindset that promotes positive change in the lives of the customers they serve.</p>
</div>

<h2 class="abs h2 test-title">TESTIMONIALS</h2>
<svg class="abs arrow" style="left:90px" width="14" height="28" viewBox="0 0 14 28" aria-hidden="true"><path d="M12 2 L2 14 L12 26" fill="none" stroke="#2fa6dc" stroke-width="2"/></svg>
<svg class="abs arrow" style="left:1116px" width="14" height="28" viewBox="0 0 14 28" aria-hidden="true"><path d="M2 2 L12 14 L2 26" fill="none" stroke="#2fa6dc" stroke-width="2"/></svg>

<blockquote class="abs quote" style="left:165px">
  <div class="mark">&ldquo;</div>
  <p>It was a training, but not your typical training. It leaves you with a new and different take on things. You will find yourself saying 'Wow, I've never thought of it like that before'. You will be left with new and refreshing ideas and different ways to approach situations.</p>
  <div class="who">Oakridge County Senior Services</div>
  <div class="mark close">&rdquo;</div>
</blockquote>
<blockquote class="abs quote" style="left:621px">
  <div class="mark">&ldquo;</div>
  <p style="margin-top:10px">Reed is easy to work with and his expertise allows you to tailor your training to the specific needs of your agency. We highly recommend Reed and his company.</p>
  <div class="who">Community Action Partnership of North Valley</div>
  <div class="mark close">&rdquo;</div>
</blockquote>

<section class="abs team"></section>
<div class="abs portrait" role="img" aria-label="Portrait photo of the CEO" style="left:158px;background:linear-gradient(160deg,#9bb27a,#3c4a5c)"></div>
<div class="abs role" style="left:347px">CEO<b>DANIEL "REED" CARVER</b></div>
<div class="abs divider"></div>
<div class="abs portrait" role="img" aria-label="Portrait photo of the CFO" style="left:634px;background:linear-gradient(160deg,#6f8f5a,#5a4438)"></div>
<div class="abs role" style="left:821px">CFO<b>MIRIAM ELLIS CARVER</b></div>

<svg class="abs footer" width="1200" height="262" viewBox="0 0 1200 262" aria-hidden="true">
  <path d="M0 20 Q 620 60 1200 -40 L1200 262 L0 262 Z" fill="#2fa6dc"/>
</svg>

<div class="abs brand" style="left:165px;top:3085px;color:#fff"><span class="brand-dot" style="background:#fff"></span>TRELMOND</div>
<div class="abs fsep" style="left:381px"></div>
<div class="abs fcol" style="left:404px"><h4>Services</h4>Training &amp; Consulting<br>Data Analytics<br>Storytelling</div>
<div class="abs fsep" style="left:603px"></div>
<div class="abs fcol" style="left:628px;top:3050px;line-height:19px"><h4>Navigation</h4>Home<br>Services<br>Roma<br>Madd<br>Resources<br>Contact</div>
<div class="abs fsep" style="left:824px"></div>
<div class="abs fcol" style="left:855px;top:3048px;line-height:21px">
  <h4>Contact Us</h4>
  <div class="contact-row"><svg width="11" height="11" viewBox="0 0 12 12"><path d="M2 1 L4.5 1 L5.5 4 L4 5 Q5 7.5 7 8 L8 6.5 L11 7.5 L11 10 Q6 11.5 1 3 Z" fill="#fff"/></svg>+61 3000 4127</div>
  <div class="contact-row"><svg width="11" height="9" viewBox="0 0 12 9"><rect x="0.5" y="0.5" width="11" height="8" fill="none" stroke="#fff"/><path d="M0.5 0.5 L6 5 L11.5 0.5" fill="none" stroke="#fff"/></svg>hello@trelmondgroup.com</div>
  <div class="contact-row" style="align-items:flex-start"><svg width="11" height="14" viewBox="0 0 11 14" style="margin-top:4px"><path d="M5.5 13 Q0.5 7 0.5 5 A5 5 0 0 1 10.5 5 Q10.5 7 5.5 13 Z" fill="#fff"/><circle cx="5.5" cy="5" r="1.8" fill="#2fa6dc"/></svg><span>48/5 Harlow St, Melbourne<br>VIC 3000, Australia</span></div>
  <div class="socials"><span></span><span></span><span></span></div>
</div>

<footer class="abs copy">Copyright © 2022 Trelmond Group. All Rights Reserved</footer>

</body>
</html>
```